National Networking/Telecommunications Company needs a new packaging (bag) design

We are currently going through a re-branding stage and need to create new packaging for all of our material.

We need a complete redesign of our current packaging (which is in various sizes). I have attached the current die-lines/knife for one of our bags.

- VORLENT logos to be changed to our PALUXO logo (attached)
- PALUXO logo to be modified, so it simply says the word PALUXO with the tick image on the end. Please remove all other writing (GRANULAR SYSTEMS & FRESH CHOICE, REMARKABLE WORTH) removed from the logo. Once this has been removed, please resize the word PALUXO, so it fits nicely beside the tick logo.
- Please remove all references to VORLENT websites, and replace with www.paluxo.com.au
- Remove "Network, Computer and Audio Video Connectivity Solutions"
- Keeping the logos that say "Lifetime Warranty" and "100% Tested and Certified", open to different ideas on how to portray them on the bag.
- Our main company colours are red, blue & silver. We're open to all designs. Packaging needs to STAND OUT, without looking cheap. Needs to still look professional and classy.
- The inside backing of the bag is to be white in colour.

I have attached our new cable box design, if that helps with keeping the colours the same.

Target Market(s)

Electrical wholesalers (who stock this product), IT/System Integrators, Installers

Industry/Entity Type

Telecommunications

Font styles to use
Sans Serif

Requirements
Must have
• Our company colours (blue, red, white/silver)
Nice to have
• Overall design needs to be simplistic, yet elegant and professional.
Should not have
• Should not have the word VORLENT anywhere

```html
<!DOCTYPE html>
<html lang="en">
<head>
<meta charset="utf-8">
<title>PALUXO Packaging Bag</title>
<link rel="stylesheet" href="https://fonts.googleapis.com/css2?family=Arimo:wght@400;700&display=swap">
<style>
  :root {
    --stage: #000000;
    --bag-white: #ffffff;
    --brand-navy: #0a1f5c;
    --brand-red: #e01f26;
    --brand-silver: #c9ccd3;
    --silver-dark: #8d929c;
    --text-dark: #1a1a1a;
  }
  * { margin: 0; padding: 0; box-sizing: border-box; }
  html, body {
    width: 1056px;
    height: 1200px;
    overflow: hidden;
    background: var(--stage);
    font-family: "Arimo", Arial, sans-serif;
  }
  .bag {
    position: absolute;
    left: 273px;
    top: 142px;
    width: 572px;
    height: 916px;
    background: var(--bag-white);
    overflow: hidden;
  }
  .bag-art {
    position: absolute;
    inset: 0;
    width: 100%;
    height: 100%;
  }
  .brand {
    position: absolute;
    left: 104px;
    top: 206px;
    display: flex;
    align-items: center;
    gap: 14px;
  }
  .brand-name {
    font-size: 67px;
    font-weight: 700;
    letter-spacing: 2px;
    color: var(--brand-silver);
    line-height: 1;
  }
  .brand-mark {
    width: 100px;
    height: 100px;
    border-radius: 50%;
    background: var(--brand-silver);
  }
  .website {
    position: absolute;
    right: 33px;
    top: 320px;
    font-size: 25px;
    color: var(--bag-white);
    line-height: 1;
  }
  .promises {
    position: absolute;
    right: 32px;
    top: 357px;
    display: flex;
    gap: 10px;
  }
  .promise-badge {
    width: 80px;
    height: 80px;
    border-radius: 50%;
    background: var(--bag-white);
    border: 4px solid var(--silver-dark);
  }
  .guarantee {
    position: absolute;
    right: 19px;
    top: 795px;
    text-align: right;
    font-size: 13.5px;
    font-weight: 700;
    line-height: 15.7px;
    color: var(--text-dark);
  }
  .guarantee p + p { margin-top: 8px; }
  .guarantee .highlight { color: var(--brand-red); font-weight: 400; }
</style>
</head>
<body>
  <main class="bag">
    <svg class="bag-art" viewBox="0 0 593 949" preserveAspectRatio="none" aria-hidden="true">
      <path class="navy-field" fill="#0a1f5c"
        d="M0 0 H593 V432 C540 475 440 490 370 482 C230 462 100 395 0 318 Z"/>
      <path class="silver-swoosh" fill="#b8bcc4"
        d="M0 272 C110 360 220 420 320 456 C200 428 90 372 0 312 Z"/>
      <path class="red-swoosh" fill="#e01f26"
        d="M372 484 C460 494 560 478 593 440 V472 C560 498 460 506 372 484 Z"/>
      <path class="hang-hole" fill="#ffffff"
        d="M258 112 H276 C280 96 312 96 316 112 H334 A12 12 0 0 1 346 124 V126 A12 12 0 0 1 334 138 H258 A12 12 0 0 1 246 126 V124 A12 12 0 0 1 258 112 Z"/>
    </svg>

    <div class="brand">
      <span class="brand-name">PALUXO</span>
      <span class="brand-mark"></span>
    </div>

    <div class="website">www.paluxo.com.au</div>

    <div class="promises">
      <span class="promise-badge"></span>
      <span class="promise-badge"></span>
    </div>

    <div class="guarantee">
      <p><span class="highlight">GUARANTEED QUALITY</span> - Independently tested<br>
      to exceed current standards and assure the<br>
      highest possible construction and quality</p>
      <p>If you are not completely satisfied with this<br>
      product please contact your PALUXO dealer or<br>
      post a comment or question on our website</p>
    </div>
  </main>
</body>
</html>
```